Package Design - Disposable Face Towel

Hi,

We are needing assistance with graphic design on our box/carton/package.

The attached image that is white is our biggest competitor.

Our brand is "BRIGHT DEW LTD." Please see the logo we uploaded.

Oder we have in mind for front of box:

Logo
LARGE TOWELS
50 Count
Ultra Soft| 100% USDA Bio-Based|100% Eucalyptus Viscose | Vegan
BRIGHTDEWLTD.EXAMPLE

We like medium to dark blue on most of the box, with white and minimal hot pink or salmon. Something that is sharp, modern, and stands out from our competitors.

Box dimensions are: 6.25 x 5.25 x 4.75 inches

This will be 1 of many design projects.

Target Market(s)

Female Beauty Products

Font styles to use
Serif
Sans Serif

Colors
0054AA
0677BA
7BADD7
CADEEF
E8F1F8
EB3D1F
EC4F4E
F09395
F8D3D4
FCEDEE

Requirements
Must have
• Needs to look sharp and modern

```html
<!DOCTYPE html>
<html lang="en">
<head>
<meta charset="utf-8">
<title>Bright Dew Ltd. – Large Towels Box Front</title>
<link rel="stylesheet" href="https://fonts.googleapis.com/css2?family=Libre+Baskerville&family=Open+Sans:wght@400;600;700&display=swap">
<style>
  :root {
    --stage: #dfe9e8;
    --box-blue: #0054aa;
    --box-blue-deep: #004a99;
    --flap-edge: #00418a;
    --accent-red: #ec4f4e;
    --strip-white: #f4f7fa;
    --ink-white: #ffffff;
    --ink-grey: #3c4650;
  }
  html, body {
    margin: 0;
    width: 1200px;
    height: 1200px;
    overflow: hidden;
    background: var(--stage);
  }
  .box-front {
    position: absolute;
    left: 100px;
    top: 220px;
    width: 1000px;
    height: 760px;
    background: var(--box-blue);
    box-shadow: 0 20px 50px rgba(0, 40, 80, 0.18);
    overflow: hidden;
  }
  .dispenser-flap {
    position: absolute;
    left: 80px;
    right: 80px;
    top: 0;
    height: 440px;
    background: var(--box-blue-deep);
    border: 3px solid var(--flap-edge);
    border-top: none;
    display: flex;
    align-items: center;
    justify-content: center;
  }
  .brand-name {
    font-family: "Libre Baskerville", serif;
    font-size: 58px;
    color: var(--ink-white);
    letter-spacing: 1px;
    margin: 0 0 70px;
  }
  .product-title {
    position: absolute;
    top: 472px;
    width: 100%;
    text-align: center;
    font-family: "Open Sans", sans-serif;
    font-weight: 400;
    font-size: 44px;
    letter-spacing: 5px;
    color: var(--ink-white);
    margin: 0;
  }
  .product-count {
    position: absolute;
    top: 532px;
    width: 100%;
    text-align: center;
    font-family: "Open Sans", sans-serif;
    font-weight: 700;
    font-size: 46px;
    letter-spacing: 4px;
    color: var(--accent-red);
    margin: 0;
  }
  .feature-band {
    position: absolute;
    top: 606px;
    left: 0;
    right: 0;
    height: 48px;
    background: var(--accent-red);
    display: flex;
    align-items: center;
    justify-content: center;
    font-family: "Open Sans", sans-serif;
    font-weight: 600;
    font-size: 24px;
    letter-spacing: 1px;
    color: var(--ink-white);
  }
  .web-strip {
    position: absolute;
    top: 654px;
    left: 0;
    right: 0;
    bottom: 0;
    background: var(--strip-white);
    display: flex;
    align-items: center;
    justify-content: center;
    font-family: "Open Sans", sans-serif;
    font-weight: 600;
    font-size: 22px;
    letter-spacing: 3px;
    color: var(--ink-grey);
  }
</style>
</head>
<body>
  <main class="box-front">
    <div class="dispenser-flap">
      <h1 class="brand-name">BRIGHT DEW LTD.</h1>
    </div>
    <p class="product-title">LARGE TOWELS</p>
    <p class="product-count">50 Count</p>
    <div class="feature-band">Ultra Soft| 100% USDA Bio-Based|100% Eucalyptus Viscose | Vegan</div>
    <div class="web-strip">BRIGHTDEWLTD.EXAMPLE</div>
  </main>
</body>
</html>
```